R&T Promotions / P.L.W. Sales Business Cards

I have 2 companies that are somewhat connected, yet sell to 2 different markets.

R&T Promotions www.rotapfx.example

We are a manufacturers representative company. We handle sales and marketing of Home Theater, Home Automation, Audio & Video products for the state of Florida. We work with Designers, Architects, Technology Consultants and Electronic Integrators to design, sell and install cutting edge technology in new and existing homes, condos and commercial spaces.

P.L.W. Sales www.plwqz.example

We are a manufacturers representative company. We handle sales and marketing of automotive Audio, Electronics, Security, Navigation and Entertainment products for the state of Florida. We work with 12-volt retailers, installers and automobile customizers to design, sell, merchandise, fabricate and install cutting edge technology in cars, boats, motor coaches, etc.

We have logo's that might still be relevant, but might need a little touching up. We need a new business card design and layout for each of the 2 companies. I would like them to have a family look, but still better speak to the customer base associated with the channel.

Target Market(s)

R&T Promotions -

Design, Engineering, Construction, Technology, elegant, tasteful.

P.L.W. Sales -

More cutting edge, industrial, youth, aggressive, fun, bold.

Industry/Entity Type

Business

Requirements
Must have
• New business card layout for both companies.
Nice to have
• A family look, or relationship to the other company. Even if it's just a logo referencing the other company.

```html
<!DOCTYPE html>
<html lang="en">
<head>
<meta charset="utf-8">
<title>R&amp;T Promotions and P.L.W. Sales – Business Cards</title>
<link rel="stylesheet" href="https://fonts.googleapis.com/css2?family=Open+Sans:wght@400&display=swap">
<style>
  :root {
    --backdrop: #3c3c3e;
    --card: #ffffff;
    --ink: #1f1f1f;
    --band: #050505;
    --swoosh: #7e8184;
    --label: #f2f2f2;
    --on-band: #ffffff;
  }
  * { margin: 0; padding: 0; box-sizing: border-box; }
  html, body { width: 941px; height: 1200px; overflow: hidden; }
  body {
    background: var(--backdrop);
    font-family: "Open Sans", "Helvetica Neue", Arial, sans-serif;
    position: relative;
  }
  .side-label {
    position: absolute;
    color: var(--label);
    font-size: 21px;
  }
  .side-label--first { left: 86px; top: 66px; }
  .side-label--second { left: 75px; top: 608px; }
  .card {
    position: absolute;
    left: 92px;
    width: 764px;
    height: 442px;
    background: var(--card);
    overflow: hidden;
    box-shadow: 0 2px 6px rgba(0,0,0,.35);
  }
  .card--rt { top: 112px; }
  .card--plw { top: 666px; }
  .card__wave {
    position: absolute;
    inset: 0;
    width: 100%;
    height: 100%;
  }
  .wave__band { fill: var(--band); }
  .wave__swoosh { fill: var(--swoosh); }
  .brand-name {
    position: absolute;
    color: var(--ink);
    font-weight: 400;
    white-space: nowrap;
  }
  .card--rt .brand-name { left: 48px; top: 60px; font-size: 27px; }
  .card--plw .brand-name {
    left: 0; right: 0; top: 98px;
    text-align: center;
    font-size: 50px;
  }
  .person {
    position: absolute;
    right: 33px;
    top: 56px;
    text-align: right;
    color: var(--ink);
  }
  .person__name { font-size: 29px; line-height: 1.15; }
  .person__role { font-size: 24px; line-height: 1.4; }
  .address {
    position: absolute;
    left: 46px;
    top: 186px;
    font-style: normal;
    font-size: 20px;
    line-height: 31px;
    color: var(--ink);
  }
  .contact-lines {
    position: absolute;
    right: 33px;
    top: 331px;
    text-align: right;
    color: var(--on-band);
    font-size: 20px;
    line-height: 30px;
    list-style: none;
    white-space: nowrap;
  }
</style>
</head>
<body>
  <p class="side-label side-label--first">Front</p>
  <section class="card card--rt">
    <svg class="card__wave" viewBox="0 0 531 307" preserveAspectRatio="none" aria-hidden="true">
      <path class="wave__swoosh" d="M0,292 C160,230 330,170 490,154 C340,172 170,238 0,304 Z"/>
      <path class="wave__band" d="M18,307 C180,245 360,176 520,160 Q531,159 531,162 L531,307 Z"/>
    </svg>
    <p class="brand-name">R&amp;T Promotions</p>
    <div class="person">
      <p class="person__name">Daniel Korwin</p>
      <p class="person__role">Rep Principle</p>
    </div>
    <address class="address">4720 NW 18th Avenue<br>Orlando, FL 32810</address>
    <ul class="contact-lines">
      <li>tel: 800-555-0142 | cell: 727 -555-0198</li>
      <li>fax: 305-555-0176 | daniel@rotapfx.example</li>
      <li>www.rotapfx.example</li>
    </ul>
  </section>

  <p class="side-label side-label--second">Front</p>
  <section class="card card--plw">
    <svg class="card__wave" viewBox="0 0 531 307" preserveAspectRatio="none" aria-hidden="true">
      <path class="wave__swoosh" d="M0,292 C160,230 330,170 490,154 C340,172 170,238 0,304 Z"/>
      <path class="wave__band" d="M18,307 C180,245 360,176 520,160 Q531,159 531,162 L531,307 Z"/>
    </svg>
    <p class="brand-name">P.L.W. Sales</p>
    <ul class="contact-lines">
      <li>daniel@plwqz.example</li>
      <li>www.plwqz.example</li>
    </ul>
  </section>
</body>
</html>
```